Business Card Project for 'Manufacturing and Healthcare Business Improvement company.

I need a business card for a consulting company that does process improvement for manufacturing and healthcare companies. I had a contest for a logo, and I liked what we came up with for the logo.

I wasn't blown away by what I got for the business card. The designer tried and it was a decent design, but I was looking for a little more. I want something that looks professional, but is eye-catching enough that people say "that looks cool, where did you get it?"

I've uploaded some business card examples I found that I liked. Even though some of the examples have red and orange on them, I think I would stick with blues, grays and blacks since that matches the logo theme. As awesome as some of them look, I don't think that a single color card, like an all-black card, will work for me; but feel free to change my mind.

It might also be possible to incorporate elements from the logo into the card. I also like some of the elements that use circles or rectangles etc to separate the phone number, website etc.

I like it when people have used geometric shapes to break up the card into sections or to add borders to the card to complement the logo, not compete with it for attention. For example, the red and gray example that has a curve that separates the card into two parts. I've wondered, how it would look if the red area were blue and had an arrow separating the top and bottom, like the arrow on the logo. Maybe on the back there could be an element that mirrors the bar graph and arrow. Would those look interesting, or would they compete with the other elements too much?

I also uploaded some examples of cards I made up, either based on ideas I saw elsewhere or based on design elements that the logo had in his designs. If you wonder why the ones with "lorem ipsum" look like an amateur did them, it's because they did.

I also think that I may add a QR code at some point, so I would need a location for that, along with something that says what the QR links to, such as, "scan here to upload contact information" or something similar. I don't know if I want cards that require having special designs cut, but if you have the idea, go with it.

I don't want to limit anyone's creativity, so I'll leave it at that.

Target Market(s)

Healthcare and Manufacturing

Industry/Entity Type

Manufacturing

Contact Information for Business Card

Harborline Advisory Partners LLC.
Gary Pruett MBA, LSSMBB
Managing Partner
g.pruett@harborlineadvisorypartnersllc.example
(555) 987-6240

Font styles to use
Serif
Sans Serif

Colors

Designer to choose only greyscale colors for use in the design.

Requirements
Must have
• The logo.
Nice to have
• Even though some of the examples I uploaded have red and orange on them, I think I would stick with blues, grays and blacks since that matches the logo theme.

I also like some of the elements that use circles or rectangles etc to separate the phone number, website etc.

I like it when people have used geometric shapes to break up the card into sections or to add borders to the card to complement the logo, not compete with it for attention.

For example, the red and gray example that has a curve that separates the card into two parts. I've wondered, how it would look if the red area were blue and had an arrow separating the top and bottom, like the arrow on the logo. Maybe on the back there could be an element that mirrors the bar graph and arrow. Would those look interesting, or would they compete with the other elements too much?

It might also be possible to incorporate elements from the logo into the card.

I also think that I may add a QR code at some point, so I would need a location for that, along with something that says what the QR links to, such as, "scan here to upload contact information" or something similar.

It could have something somewhere saying "We use Lean, Six Sigma and TPM continuous improvement tools to improve manufacturing and healthcare businesses."
Should not have
• So many colors and elements that it is distracting. Should not be generic.

As awesome as some of them look, I don't think that a single color card, like an all-black card, will work for me; but feel free to change my mind.

I don't know if I want cards that require having special designs cut, but if you have the idea, go with it.

```html
<!DOCTYPE html>
<html lang="en">
<head>
<meta charset="utf-8">
<title>Harborline Advisory Partners LLC. – Business Card</title>
<link href="https://fonts.googleapis.com/css2?family=Roboto:wght@400;500;700&display=swap" rel="stylesheet">
<style>
  :root {
    --backdrop: #232325;
    --navy: #1c3566;
    --navy-deep: #172c56;
    --navy-faint: #22407a;
    --ink: #1b2a55;
    --text-dark: #222630;
    --paper: #ffffff;
  }
  * { box-sizing: border-box; margin: 0; padding: 0; }
  html, body {
    width: 1200px; height: 1200px; overflow: hidden;
    background: var(--backdrop);
    font-family: "Roboto", Arial, sans-serif;
  }
  .stage { position: relative; width: 1200px; height: 1200px; }
  .card {
    position: absolute; left: 284px; width: 615px; height: 369px;
  }
  .card-front { top: 235px; background: var(--navy); }
  .card-back { top: 644px; background: var(--paper); }

  .front-wordmark {
    position: absolute; left: 156px; top: 140px; width: 305px;
    color: var(--navy-deep); font-weight: 700; text-align: center;
    font-size: 30px; line-height: 1.1; letter-spacing: 0.5px;
  }
  .front-wordmark-echo {
    position: absolute; left: 330px; top: 238px; width: 245px;
    color: var(--navy-faint); font-weight: 700; text-align: center;
    font-size: 22px; line-height: 1.1;
  }

  .brand {
    position: absolute; left: 92px; top: 140px; width: 200px;
    display: flex; align-items: center; gap: 10px;
  }
  .brand-square { width: 22px; height: 22px; background: var(--navy); flex: none; }
  .brand-name {
    color: var(--navy); font-weight: 700; font-size: 19px; line-height: 1.15;
  }

  .divider {
    position: absolute; left: 307px; top: 125px; width: 1.5px; height: 116px;
    background: var(--navy);
  }
  .details { position: absolute; left: 323px; top: 124px; }
  .person-name {
    color: var(--ink); font-weight: 700; font-size: 21px; line-height: 1;
  }
  .credentials {
    margin-top: 6px; color: var(--text-dark); font-weight: 500; font-size: 12px;
  }
  .company {
    margin-top: 31px; color: var(--ink); font-weight: 700; font-size: 12.3px;
  }
  .contact-line {
    display: flex; align-items: center; gap: 5px; margin-top: 5px;
    color: var(--text-dark); font-size: 11px; font-weight: 400;
  }
  .contact-line svg { width: 10px; height: 10px; flex: none; }
</style>
</head>
<body>
<main class="stage">
  <section class="card card-front">
    <div class="front-wordmark">Harborline Advisory<br>Partners LLC.</div>
    <div class="front-wordmark-echo">Harborline Advisory<br>Partners LLC.</div>
  </section>

  <section class="card card-back">
    <div class="brand">
      <span class="brand-square"></span>
      <span class="brand-name">Harborline Advisory Partners LLC.</span>
    </div>
    <div class="divider"></div>
    <div class="details">
      <p class="person-name">GARY PRUETT</p>
      <p class="credentials">MBA, LSSMBB</p>
      <p class="company">HARBORLINE ADVISORY PARTNERS LLC.</p>
      <p class="contact-line">
        <svg viewBox="0 0 10 10" aria-hidden="true"><rect x="0.5" y="2" width="9" height="6.5" fill="none" stroke="#1b2a55" stroke-width="1.2"/><path d="M0.8 2.4 L5 5.6 L9.2 2.4" fill="none" stroke="#1b2a55" stroke-width="1.2"/></svg>
        g.pruett@harborlineadvisorypartnersllc.example
      </p>
      <p class="contact-line">
        <svg viewBox="0 0 10 10" aria-hidden="true"><path d="M2 0.8 L3.6 2.8 L2.7 4 Q3.8 6.2 6 7.3 L7.2 6.4 L9.2 8 L8 9.4 Q4.5 9.2 2.6 7.4 Q0.8 5.5 0.6 2 Z" fill="#1b2a55"/></svg>
        (555) 987-6240
      </p>
    </div>
  </section>
</main>
</body>
</html>
```